Bookkeeping business needs a digital and print flyer

We need a flyer to promote our virtual bookkeeping services to small and mid-sized businesses in the United States. We want the content and design of the flyer to be consistent with our website: www.brightledgerbookkeeping.example. We would like both a print version and a digital version of the flyer.

```html
<!DOCTYPE html>
<html lang="en">
<head>
<meta charset="utf-8">
<title>Bright Ledger Bookkeeping – Flyers</title>
<link rel="stylesheet" href="https://fonts.googleapis.com/css2?family=Montserrat:ital,wght@0,400;0,500;0,600;0,700;0,800;0,900;1,400;1,500&family=Great+Vibes&display=swap">
<style>
:root{
  --yellow:#fcc02e;
  --yellow-soft:#fde7a6;
  --cream:#fdf8ea;
  --black:#121212;
  --white:#ffffff;
  --ink:#1c1c1c;
  --grey-bg:#efefef;
  --shadow:#d9d9d9;
}
*{margin:0;padding:0;box-sizing:border-box}
html,body{width:1200px;height:1200px;overflow:hidden;background:var(--grey-bg)}
body{position:relative;font-family:'Montserrat',sans-serif;color:var(--ink)}
.flyer{position:absolute;top:236px;width:430px;height:555px;transform:scale(1.2245);transform-origin:0 0;overflow:hidden;background:var(--white);box-shadow:0 1px 3px rgba(0,0,0,.12)}
.flyer--problems{left:55px;background:var(--cream)}
.flyer--about{left:617px}
.abs{position:absolute}

/* header */
.header{position:absolute;left:0;top:0;width:430px;height:57px;background:var(--yellow)}
.header svg{position:absolute;left:0;top:0}
.brand{position:absolute;left:9px;top:16px;display:flex;align-items:center;gap:6px;color:var(--white);font-weight:400;letter-spacing:.5px}
.brand__name{font-size:11.5px;line-height:1.05}
.brand__dot{width:17px;height:17px;border-radius:50%;border:1.5px solid var(--white)}
.header__title{position:absolute;left:203px;top:12px;text-align:center;width:220px;font-weight:800;line-height:1.1}
.header__title b{display:block;font-size:14.5px;font-weight:900;letter-spacing:.2px}
.header__title span{display:block;font-size:14px;font-weight:600;letter-spacing:.6px}

/* photo placeholders */
.photo{position:absolute;border-radius:50%;border:5px solid var(--yellow)}
.photo--desk{left:-12px;top:48px;width:200px;height:162px;background:linear-gradient(140deg,#c9c6c1,#8f8b86 55%,#e6e0d6)}
.photo--sunset{left:18px;top:335px;width:150px;height:150px;background:linear-gradient(180deg,#b79ab0 0%,#f2c37a 55%,#3a2a25 100%)}
.photo--portrait{left:6px;top:306px;width:130px;height:205px;border:none;border-radius:0;background:linear-gradient(180deg,#dcdcdc,#9aa0aa 60%,#2e3142)}

/* headings & lists */
.heading{font-weight:800;font-size:16.5px;color:var(--black)}
.dots{height:0;border-top:2px dotted var(--yellow)}
.questions{list-style:none;font-style:italic;font-size:8.3px;line-height:10.4px;color:#333}
.questions li{padding-left:7px;position:relative}
.questions li::before{content:"•";position:absolute;left:0;color:var(--yellow);font-style:normal}
.checks{list-style:none;font-size:9.4px;line-height:11.7px}
.checks li{position:relative;padding-left:13px}
.checks li::before{content:"";position:absolute;left:0;top:2px;width:8px;height:8px;border:1px solid var(--yellow);border-radius:50%}
.checks li::after{content:"";position:absolute;left:3px;top:3.5px;width:2.5px;height:4px;border:solid var(--yellow);border-width:0 1.3px 1.3px 0;transform:rotate(45deg)}

/* hello pill */
.hello{left:73px;top:238px;width:278px}
.hello__pill{background:var(--black);color:var(--white);text-align:center;border-radius:7px;padding:5px 6px 4px;font-weight:700;font-size:14.2px;line-height:17px;position:relative;z-index:1}
.hello__pill em{font-style:normal;color:var(--yellow)}
.hello__sub{background:var(--yellow);margin-top:-4px;padding:7px 4px 4px;text-align:center;font-size:7.4px;font-weight:700;line-height:9px;border-radius:0 0 5px 5px}
.services-title{font-weight:800;font-size:12px;letter-spacing:.3px}

/* footer */
.footer{position:absolute;left:0;top:522px;width:430px;height:33px;background:var(--yellow);display:flex;align-items:center;justify-content:space-between;padding:0 8px;font-size:6.6px;font-weight:700}
.footer__item{display:flex;align-items:center;gap:4px}
.footer__item svg{flex:none}
.waves{position:absolute;left:0;top:488px}

/* about flyer */
.tailored{left:13px;top:70px;font-weight:700;font-size:14.5px;line-height:19px;color:var(--black)}
.tailored em{font-style:normal;color:var(--yellow)}
.badge{position:absolute;top:137px;width:42px;height:52px;background:var(--white);border:1px solid #ddd}
.badge i{position:absolute;left:9px;top:8px;width:24px;height:24px;border-radius:50%}
.intro{left:222px;top:70px;width:200px;color:var(--white);font-weight:700;font-size:9.2px;line-height:11.5px}
.outsource{left:222px;top:106px;color:var(--yellow);font-weight:800;font-size:12px}
.checks--light{color:var(--white);font-size:8.3px;line-height:10.2px}
.quote-box{left:76px;top:232px;width:278px;height:62px;background:var(--yellow);border-radius:9px;box-shadow:6px 6px 0 var(--shadow);display:flex;align-items:center;justify-content:center;text-align:center;font-size:15.5px;line-height:19px;font-weight:500}
.meet{left:143px;top:310px;font-family:'Great Vibes',cursive;font-size:27px;color:var(--black)}
.bio{left:143px;top:350px;width:282px;font-size:7.2px;line-height:9.2px;color:#333}
.bio__line{display:block}
.bio--caps{top:408px;font-weight:800;text-transform:uppercase;color:var(--black)}
.values{left:143px;top:449px;width:272px;height:21px;border-radius:11px;background:var(--black);color:var(--yellow);font-weight:800;font-size:10.5px;display:flex;align-items:center;justify-content:center;letter-spacing:.6px;word-spacing:2px}
.cta{left:160px;top:478px;font-size:11px;font-weight:500}
.cta b{color:var(--yellow);font-weight:800}
</style>
</head>
<body>

<section class="flyer flyer--problems">
  <svg class="abs" style="left:0;top:0" width="430" height="555" aria-hidden="true">
    <path d="M0 352 Q215 268 430 352" fill="none" stroke="var(--yellow)" stroke-width="1.5"/>
  </svg>

  <div class="photo photo--desk" role="img" aria-label="Photo of a stressed man at a cluttered desk covered in papers"></div>

  <header class="header">
    <svg width="200" height="57" aria-hidden="true"><path d="M0 0 H182 Q156 28 148 57 H0 Z" fill="var(--black)"/></svg>
    <div class="brand"><span class="brand__name">BRIGHT LEDGER<br>BOOKKEEPING</span><span class="brand__dot"></span></div>
    <div class="header__title"><b>VIRTUAL BOOKKEEPING</b><span>FOR SMALL BUSINESS</span></div>
  </header>

  <h2 class="heading abs" style="left:233px;top:62px">Overwhelmed?</h2>
  <div class="dots abs" style="left:233px;top:85px;width:135px"></div>
  <ul class="questions abs" style="left:233px;top:92px;width:195px">
    <li>Do you feel pulled in so many directions you don't know which way is up?</li>
    <li>Do you hate that shoebox of receipts sitting on your desk?</li>
    <li>Do you wish you could just do the parts of your business that you enjoy?</li>
    <li>Do you dread logging into Tallybook?</li>
    <li>Do you panic at tax time?</li>
    <li>Do you feel like you've lost control of your finances?</li>
    <li>Do you wish you could pay yourself more but aren't sure if you can?</li>
  </ul>

  <div class="hello abs">
    <div class="hello__pill">Say Hello to a reliable, hassle-free<br>BOOKKEEPING <em>SOLUTION!</em></div>
    <div class="hello__sub">Build your business by focusing on what you love,<br>not what drains the life out of you!</div>
  </div>

  <div class="photo photo--sunset" role="img" aria-label="Photo of a person with arms outstretched against a sunset over the sea"></div>

  <h3 class="services-title abs" style="left:190px;top:325px">SERVICES AVAILABLE:</h3>
  <div class="dots abs" style="left:190px;top:342px;width:65px"></div>
  <ul class="checks abs" style="left:177px;top:350px;width:250px">
    <li>Catch-up and clean-up services</li>
    <li>Transaction importation and categorization</li>
    <li>Monthly reconciliation of all accounts,<br>including assets and loans.</li>
    <li>Monthly financial reports<br>(Balance Sheet, Income Statement, Cash Flow)</li>
    <li>Monthly video conference</li>
    <li>Annual tax-prep package sent to your preparer<br>A/R &amp; A/P</li>
    <li>Payroll coordination 1099s</li>
    <li>Bill pay &amp; receipt management</li>
    <li>Budgeting</li>
  </ul>

  <svg class="waves" width="430" height="40" aria-hidden="true">
    <path d="M0 18 Q60 4 130 14 T270 12 T430 6 V40 H0 Z" fill="var(--yellow-soft)"/>
    <path d="M0 26 Q80 14 160 24 T320 20 T430 16 V40 H0 Z" fill="var(--yellow)"/>
  </svg>
  <footer class="footer">
    <span class="footer__item"><svg width="12" height="12" viewBox="0 0 12 12"><circle cx="6" cy="6" r="6" fill="var(--white)"/><path d="M4 3 l1.2 1.4 -.6.8 q.6 1.4 2 2 l.8-.6 1.4 1.2 -.8 1 q-3.2-.4-5-4.6z" fill="var(--black)"/></svg>555-014-2760</span>
    <span class="footer__item"><svg width="12" height="12" viewBox="0 0 12 12"><circle cx="6" cy="6" r="6" fill="var(--white)"/><rect x="3" y="4" width="6" height="4.2" fill="none" stroke="var(--black)" stroke-width=".8"/><path d="M3 4 L6 6.4 L9 4" fill="none" stroke="var(--black)" stroke-width=".8"/></svg>CLARA@BRIGHTLEDGERBOOKKEEPING.EXAMPLE</span>
    <span class="footer__item"><svg width="12" height="12" viewBox="0 0 12 12"><circle cx="6" cy="6" r="6" fill="var(--white)"/><circle cx="6" cy="6" r="3.2" fill="none" stroke="var(--black)" stroke-width=".8"/><path d="M2.8 6 H9.2 M6 2.8 Q4.2 6 6 9.2 Q7.8 6 6 2.8" fill="none" stroke="var(--black)" stroke-width=".7"/></svg>BRIGHTLEDGERBOOKKEEPING.EXAMPLE</span>
  </footer>
</section>

<section class="flyer flyer--about">
  <svg class="abs" style="left:0;top:0" width="430" height="300" aria-hidden="true">
    <path d="M0 40 H430 V232 Q260 205 0 230 Z" fill="var(--black)"/>
    <path d="M0 236 Q260 211 430 238" fill="none" stroke="var(--yellow)" stroke-width="2"/>
    <circle cx="62" cy="125" r="136" fill="var(--white)" stroke="var(--yellow)" stroke-width="5"/>
  </svg>

  <header class="header">
    <svg width="200" height="57" aria-hidden="true"><path d="M0 0 H182 Q156 28 148 57 H0 Z" fill="var(--black)"/></svg>
    <div class="brand"><span class="brand__name">BRIGHT LEDGER<br>BOOKKEEPING</span><span class="brand__dot"></span></div>
    <div class="header__title"><b>VIRTUAL BOOKKEEPING</b><span>FOR SMALL BUSINESS</span></div>
  </header>

  <h2 class="tailored abs">Bookkeeping<br>Tailored to <em>YOUR</em><br>Business Needs</h2>
  <div class="badge" style="left:14px"><i style="background:#7dbb42"></i></div>
  <div class="badge" style="left:62px"><i style="background:#6a4fa3"></i></div>

  <p class="intro abs">Take charge of your business and concentrate on your strengths to become its hero!</p>
  <p class="outsource abs">Outsource your bookkeeping!</p>
  <div class="dots abs" style="left:222px;top:124px;width:190px"></div>
  <ul class="checks checks--light abs" style="left:209px;top:130px;width:215px">
    <li>Take back your time</li>
    <li>Do more of what you love</li>
    <li>Focus on your strengths and what you do best</li>
    <li>Confidently make business decisions</li>
    <li>Sail through tax time</li>
    <li>Save over the expense of a full-time employee</li>
    <li>Pay yourself more</li>
    <li>Experience financial peace</li>
  </ul>

  <div class="quote-box abs">I love the entrepreneurial spirit<br>of small business owners!</div>
  <svg class="abs" style="left:355px;top:212px" width="34" height="30" aria-hidden="true">
    <path d="M3 28 Q1 10 14 2 L15 6 Q9 11 11 17 Q16 19 14 25 Q10 30 3 28Z M19 28 Q17 10 30 2 L31 6 Q25 11 27 17 Q32 19 30 25 Q26 30 19 28Z" fill="var(--black)"/>
  </svg>

  <svg class="abs" style="left:0;top:300px" width="150" height="200" aria-hidden="true">
    <g stroke="#e6e6e6" stroke-width="5" stroke-linecap="round">
      <path d="M70 40 L62 12"/><path d="M48 52 L30 28"/><path d="M34 72 L8 58"/><path d="M28 96 L2 94"/><path d="M98 40 L104 12"/><path d="M120 52 L138 28"/>
    </g>
  </svg>
  <div class="photo photo--portrait" role="img" aria-label="Portrait photo of the bookkeeper, a woman with long hair and glasses in a navy blouse"></div>

  <h3 class="meet abs">Meet Clara</h3>
  <p class="bio abs">
    <span class="bio__line">Being a small business owner is tough and I can totally relate.</span>
    <span class="bio__line">Between bookkeeping and trying to balance business &amp; personal life,</span>
    <span class="bio__line">it can get overwhelming. I'm all about supporting entrepreneurs &amp;</span>
    <span class="bio__line">helping small business owners reach their goals.</span>
    <span class="bio__line">Let's take your business to the next level together!</span>
  </p>
  <div class="dots abs" style="left:143px;top:401px;width:205px"></div>
  <p class="bio bio--caps abs">I want to do more than just help you get by.<br>My goal is to help you succeed and do well in all areas<br>of your life.</p>
  <div class="values abs">HEART • SOUL • MIND • STRENGTH</div>
  <p class="cta abs"><b>FREE CONSULTATION!</b> Let's work together!</p>

  <svg class="waves" width="430" height="40" aria-hidden="true">
    <path d="M0 18 Q60 4 130 14 T270 12 T430 6 V40 H0 Z" fill="var(--yellow-soft)"/>
    <path d="M0 26 Q80 14 160 24 T320 20 T430 16 V40 H0 Z" fill="var(--yellow)"/>
  </svg>
  <footer class="footer">
    <span class="footer__item"><svg width="12" height="12" viewBox="0 0 12 12"><circle cx="6" cy="6" r="6" fill="var(--white)"/><path d="M4 3 l1.2 1.4 -.6.8 q.6 1.4 2 2 l.8-.6 1.4 1.2 -.8 1 q-3.2-.4-5-4.6z" fill="var(--black)"/></svg>555-014-2760</span>
    <span class="footer__item"><svg width="12" height="12" viewBox="0 0 12 12"><circle cx="6" cy="6" r="6" fill="var(--white)"/><rect x="3" y="4" width="6" height="4.2" fill="none" stroke="var(--black)" stroke-width=".8"/><path d="M3 4 L6 6.4 L9 4" fill="none" stroke="var(--black)" stroke-width=".8"/></svg>CLARA@BRIGHTLEDGERBOOKKEEPING.EXAMPLE</span>
    <span class="footer__item"><svg width="12" height="12" viewBox="0 0 12 12"><circle cx="6" cy="6" r="6" fill="var(--white)"/><circle cx="6" cy="6" r="3.2" fill="none" stroke="var(--black)" stroke-width=".8"/><path d="M2.8 6 H9.2 M6 2.8 Q4.2 6 6 9.2 Q7.8 6 6 2.8" fill="none" stroke="var(--black)" stroke-width=".7"/></svg>BRIGHTLEDGERBOOKKEEPING.EXAMPLE</span>
  </footer>
</section>

</body>
</html>
```